Business Card Design Project

We are looking for a new business card design for a Drilling company in WA, Australia.

We are in between offices, however require a design in the meantime due to some upcoming events with our basic information.

The Logo for our company is Blue and Grey and would like this colour scheme throughout.

We are quite a new company so would like a memorable design that stands out and communicates a strong commitment to safety, quality of work and performance.

The company name is Ironbark Boring Group (IBG)

The details to be included are as follows:

Gavin Thorley
Managing Director
m.0481639207
e.gavin@ibgpty.com.au

Martin Thorley
Director
m.0419852637
e.martin@ibgpty.com.au

Industry/Entity Type

Events

Requirements
Must have
• Under the Logo, we would like 'Western Australia'

```html
<!DOCTYPE html>
<html lang="en">
<head>
<meta charset="utf-8">
<title>Ironbark Boring Group – Business Cards</title>
<link rel="stylesheet" href="https://fonts.googleapis.com/css2?family=Ubuntu:wght@400;500;700&display=swap">
<style>
  :root {
    --bg: #e9ecee;
    --card-grey: #8b8c8e;
    --card-white: #ffffff;
    --brand-blue: #1d4a93;
    --text-grey: #5b5d60;
    --soft-grey: #d9dadc;
    --white: #ffffff;
    --shadow: 0 6px 18px rgba(30, 40, 50, 0.18);
  }
  * { box-sizing: border-box; margin: 0; padding: 0; }
  html, body {
    width: 1200px;
    height: 960px;
    overflow: hidden;
    background: var(--bg);
    font-family: "Ubuntu", Arial, sans-serif;
  }
  .sheet {
    position: relative;
    width: 1200px;
    height: 960px;
  }
  .card {
    position: absolute;
    width: 570px;
    height: 350px;
    border-radius: 4px;
    box-shadow: var(--shadow);
    overflow: hidden;
  }

  /* Front */
  .card--front {
    left: 315px;
    top: 90px;
    background: var(--card-grey);
    display: flex;
    align-items: center;
    justify-content: center;
  }
  .brand {
    display: flex;
    align-items: flex-start;
    gap: 14px;
  }
  .brand__mark {
    flex: none;
    width: 26px;
    height: 26px;
    margin-top: 6px;
    background: var(--white);
  }
  .brand__text {
    display: flex;
    flex-direction: column;
  }
  .brand__name {
    font-weight: 700;
    font-size: 34px;
    line-height: 1.1;
    letter-spacing: 0.5px;
    color: var(--white);
    text-transform: uppercase;
    white-space: nowrap;
  }
  .brand__region {
    margin-top: 6px;
    font-weight: 400;
    font-size: 14px;
    letter-spacing: 4px;
    color: var(--soft-grey);
    text-transform: uppercase;
  }

  /* Back */
  .card--back {
    top: 500px;
    background: var(--card-white);
  }
  .card--gavin { left: 20px; }
  .card--martin { left: 610px; }
  .card--back .brand {
    position: absolute;
    left: 38px;
    top: 36px;
    gap: 10px;
  }
  .card--back .brand__mark {
    width: 15px;
    height: 15px;
    margin-top: 4px;
    background: var(--brand-blue);
  }
  .card--back .brand__name {
    font-size: 19px;
    color: var(--brand-blue);
  }
  .card--back .brand__region {
    margin-top: 4px;
    font-size: 10px;
    letter-spacing: 3px;
    color: var(--text-grey);
  }
  .person {
    position: absolute;
    left: 38px;
    top: 130px;
    color: var(--text-grey);
  }
  .person__name {
    font-size: 21px;
    font-weight: 400;
    letter-spacing: 1.5px;
    text-transform: uppercase;
  }
  .person__role {
    font-size: 16px;
    margin-top: 4px;
    letter-spacing: 0.5px;
  }
  .contact {
    position: absolute;
    left: 38px;
    top: 236px;
    list-style: none;
    font-size: 15px;
    color: var(--text-grey);
    line-height: 28px;
    letter-spacing: 0.5px;
  }
  .contact__label {
    color: var(--brand-blue);
    font-weight: 500;
    display: inline-block;
    width: 16px;
  }
</style>
</head>
<body>
  <main class="sheet">
    <section class="card card--front" aria-label="Card front">
      <div class="brand">
        <span class="brand__mark" aria-hidden="true"></span>
        <div class="brand__text">
          <span class="brand__name">Ironbark Boring Group</span>
          <span class="brand__region">Western Australia</span>
        </div>
      </div>
    </section>

    <section class="card card--back card--gavin" aria-label="Card back, Gavin Thorley">
      <div class="brand">
        <span class="brand__mark" aria-hidden="true"></span>
        <div class="brand__text">
          <span class="brand__name">Ironbark Boring Group</span>
          <span class="brand__region">Western Australia</span>
        </div>
      </div>
      <div class="person">
        <h1 class="person__name">Gavin Thorley</h1>
        <p class="person__role">Managing Director</p>
      </div>
      <ul class="contact">
        <li><span class="contact__label">m</span> : 0481639207</li>
        <li><span class="contact__label">e</span> : gavin@ibgpty.com.au</li>
      </ul>
    </section>

    <section class="card card--back card--martin" aria-label="Card back, Martin Thorley">
      <div class="brand">
        <span class="brand__mark" aria-hidden="true"></span>
        <div class="brand__text">
          <span class="brand__name">Ironbark Boring Group</span>
          <span class="brand__region">Western Australia</span>
        </div>
      </div>
      <div class="person">
        <h2 class="person__name">Martin Thorley</h2>
        <p class="person__role">Director</p>
      </div>
      <ul class="contact">
        <li><span class="contact__label">m</span> : 0419852637</li>
        <li><span class="contact__label">e</span> : martin@ibgpty.com.au</li>
      </ul>
    </section>
  </main>
</body>
</html>
```